Rather Likely The Brightest Venture
Website for Life Coach
Rather Likely The Brightest Venture - Personal Care
Creative Brief
Personal Care
www.bluelanternhour.com
Website design for inspirational and motivational training company. Initial focus of the website is to promote trainer for life coach and inspirational speaker engagements with plan to expend into seminar and web based trainings in 2013.
General feel to be very upbeat, happy, feel good, simple and easy to navigate. !!When referring to the holding page of Blue Lantern Hour (which I think looks crap) please note the writing in the Logo of the name should be in Black!!
left side
http://www.quostelbury.com/
http://www.drwabble.com/
http://www.nora-pellham.com/
Home page to include areas for the following: Top banner showing logo, quote and small picture of face of company. Below this a thicker banner with sunflower field picture (in future to be a video link) and beside it text of an inspirational quote that will change on a regular basis. This to also include an opt in button where they can provide email address to be contacted or receive blogs and articles direct to their account. Links to other pages: home, the way, live it, who is he, contact me, archive Home page to also include a Short text intro to what blue lantern hour is all about with a picture of face of company again. Below this Space for most recent blog or article in full (to be changed on a regular basis) Opt in button at bottom of page Links at bottom of page to affiliated websites The opt in button to be at top and bottom of all pages with affiliate web links at bottom of all pages. Additional pages: The Way: A page describing the lifestyle being coached and it's different sections. There are 6 text sections in total on this page, each with a matching inspirational image to it. Live It: Introducing the concept of coaching. Images and text again with one testimonial at the top and a list of testimonials at the bottom Who Is He: A simply text and images page for bio information Contact: listing of ways in which to contact me. Also a space where they can fill out name, contact, and question or request. The submit button will automatically send this to an email. Archive: a simple listing of previous blogs and articles. These to be listed at top with a click on link to where they are further down the page

```html
<!DOCTYPE html>
<html lang="en">
<head>
<meta charset="utf-8">
<title>Blue Lantern Hour</title>
<link href="https://fonts.googleapis.com/css2?family=Arimo:wght@400;700&family=Gochi+Hand&display=swap" rel="stylesheet">
<style>
:root{
  --page-bg:#ffffff;
  --navy-900:#141a27;
  --navy-800:#1c2333;
  --navy-700:#252e42;
  --navy-600:#313c55;
  --steel:#4a5672;
  --yellow:#f6c300;
  --hero-gold:#c9a928;
  --hero-olive:#8a8a3a;
  --text-light:#e7ebf2;
  --text-muted:#9aa4b8;
  --text-dim:#6f7a90;
  --white:#ffffff;
}
*{box-sizing:border-box;margin:0;padding:0}
html,body{width:1200px;height:866px;overflow:hidden;background:var(--page-bg);font-family:"Arimo",Arial,sans-serif}
.canvas{position:relative;width:1200px;height:866px}
.site{position:absolute;left:180px;top:0;width:840px;height:858px;background:var(--navy-800);box-shadow:0 0 18px rgba(0,0,0,.35)}
.ticker{position:absolute;left:0;top:0;width:100%;height:22px;background:var(--yellow);color:#2a2a2a;font-size:10px;font-weight:700;line-height:22px;white-space:nowrap;overflow:hidden;padding-left:120px}
.header{position:absolute;left:0;top:22px;width:100%;height:108px;background:linear-gradient(180deg,#2a3348,#1c2333)}
.brand{position:absolute;left:84px;top:30px;display:flex;align-items:center;gap:10px}
.brand-dot{width:42px;height:42px;border-radius:50%;background:var(--yellow)}
.brand-name{color:var(--white);font-size:20px;font-weight:700}
.tagline{position:absolute;left:360px;top:18px;font-family:"Gochi Hand",cursive;color:var(--white);font-size:26px;line-height:28px;text-align:left;width:240px}
.tagline-mark{color:var(--yellow)}
.team-photo{position:absolute;right:36px;top:10px;width:166px;height:82px;background:linear-gradient(180deg,#c9cdd6,#8a93a6);border:3px solid var(--white)}
.main-nav{position:absolute;left:80px;top:142px;width:124px;list-style:none}
.main-nav li{height:33px;line-height:30px;padding-left:14px;color:var(--text-muted);font-size:15px;font-weight:700}
.main-nav li.active{background:var(--navy-600);color:var(--white)}
.hero{position:absolute;left:216px;top:132px;width:576px;height:216px;background:var(--white);padding:8px}
.hero-image{width:100%;height:100%;background:linear-gradient(135deg,var(--hero-gold),var(--hero-olive))}
.slider-dots{position:absolute;left:484px;top:352px;display:flex;gap:5px}
.slider-dots span{width:9px;height:9px;border-radius:50%;background:var(--steel)}
.slider-dots span.on{background:var(--text-light)}
.quote{position:absolute;left:110px;top:364px;width:640px;font-family:"Gochi Hand",cursive;color:var(--text-light);font-size:21px;line-height:23px}
.quote-author{font-family:"Arimo",sans-serif;font-size:9px;color:var(--text-muted);margin-left:8px}
.features{position:absolute;left:60px;top:432px;width:720px;height:220px;display:grid;grid-template-columns:repeat(4,1fr);gap:6px}
.card{background:var(--navy-700);border:1px solid var(--navy-600)}
.card-head{height:26px;background:linear-gradient(180deg,#3c4864,#2b3449);color:var(--white);font-size:12px;font-weight:700;display:flex;align-items:center;gap:6px;padding-left:8px;white-space:nowrap}
.card-head svg{flex:none}
.card-body{padding:8px;font-size:8px;line-height:11px;color:var(--text-muted)}
.card-photo{height:54px;margin-bottom:6px}
.card-title{color:var(--yellow);font-size:11px;font-weight:700;margin-bottom:4px}
.btn{display:inline-block;background:var(--yellow);color:#222;font-size:8px;font-weight:700;padding:4px 8px;margin-top:8px}
.contact-row{display:flex;gap:8px;align-items:center;margin-bottom:5px}
.contact-row b{display:block;color:var(--text-light);font-size:8px}
.testimonials{margin-top:8px;color:var(--yellow);font-size:12px;font-family:"Gochi Hand",cursive}
.field-label{color:var(--text-light);font-size:8px;font-weight:700;margin-top:5px}
.field{height:14px;background:#d7dbe3;margin-top:2px}
.join-lead{color:var(--yellow);font-weight:700;margin-top:6px;font-size:9px}
.footer{position:absolute;left:0;top:672px;width:100%;height:150px;background:var(--navy-900)}
.footer-col{position:absolute;top:14px}
.footer-col h3{color:var(--text-light);font-size:16px;font-weight:700;margin-bottom:6px}
.footer-col ul{list-style:none;font-size:9px;line-height:12px;color:var(--text-dim)}
.affiliate-grid{display:grid;grid-template-columns:repeat(4,32px);gap:6px 8px;margin-top:4px}
.affiliate-grid div{height:28px;border:1px solid var(--steel)}
.news li{color:var(--text-muted);margin-bottom:3px}
.news-badge{position:absolute;right:-14px;top:0;width:18px;height:18px;background:var(--yellow);border-radius:3px}
.bottom-bar{position:absolute;left:0;top:822px;width:100%;height:36px;background:linear-gradient(180deg,#eef0f3,#c9ced6);display:flex;align-items:center;justify-content:space-between;padding:0 14px;font-size:8px;color:#555}
.bottom-nav{display:flex;gap:10px;font-weight:700;color:#333}
.bottom-mail{display:flex;align-items:center;gap:5px;font-weight:700;color:#333}
</style>
</head>
<body>
<div class="canvas">
  <div class="site">
    <div class="ticker">Welcome to "Blue Lantern Hour" &nbsp; The Fast Track Tools to a Better Life. &nbsp; Welcome to "Blue Lantern Hour" &nbsp; The Fast Track Tools to a Better Life. &nbsp; Welcome to "Blue Lantern Hour"</div>

    <header class="header">
      <div class="brand"><span class="brand-dot"></span><span class="brand-name">Blue Lantern Hour</span></div>
      <p class="tagline"><span class="tagline-mark">“</span> Life is too short for it to be this way. <span class="tagline-mark">”</span></p>
      <div class="team-photo" role="img" aria-label="Small photo of the company's people"></div>
    </header>

    <ul class="main-nav">
      <li class="active">Home</li>
      <li>The Way</li>
      <li>Live It</li>
      <li>Who Is He</li>
      <li>Contact Me</li>
      <li>Archive</li>
    </ul>

    <div class="hero"><div class="hero-image" role="img" aria-label="Photo of a sunflower field under a blue sky"></div></div>
    <div class="slider-dots"><span class="on"></span><span></span><span></span><span></span></div>

    <p class="quote">“ Living each day as your favorite is a simple matter of choice. And the power of that choice lies within you. ” <span class="quote-author">- Ellis Varran, Blue Lantern Hour</span></p>

    <section class="features">
      <article class="card">
        <div class="card-head"><svg width="12" height="12"><rect x="1" y="1" width="10" height="10" fill="#f6c300"/></svg>About Blue Lantern Hour</div>
        <div class="card-body">
          <div class="card-photo" role="img" aria-label="Colourful pencils photo" style="background:linear-gradient(135deg,#d9763f,#c9a03a)"></div>
          <div class="card-title">About Blue Lantern Hour</div>
          Caught up in a busy, non-stop world? Tired of doing the same things day after day? Feel like there is no time for you? Life is too short for it to be this way.
          <br><span class="btn">Learn More</span>
        </div>
      </article>
      <article class="card">
        <div class="card-head"><svg width="12" height="12"><rect x="1" y="1" width="10" height="10" fill="#f6c300"/></svg>Our Blog Updates</div>
        <div class="card-body">
          <div class="card-photo" role="img" aria-label="Photo of a person with arms raised in a green field" style="background:linear-gradient(135deg,#8fb7d6,#93b466)"></div>
          <div class="card-title">My Personal Experience</div>
          What is just like one of your favorite days, we could choose to live every day with passion, laughter and joy? It's quite simply a choice we make.
          <br><span class="btn">All Comments</span> <span class="btn">Read More</span>
        </div>
      </article>
      <article class="card">
        <div class="card-head"><svg width="12" height="12"><rect x="1" y="1" width="10" height="10" fill="#f6c300"/></svg>Our Contact</div>
        <div class="card-body">
          <div class="contact-row"><svg width="14" height="14"><rect x="3" y="1" width="8" height="12" rx="2" fill="#e7ebf2"/></svg><div><b>PHONE</b>(208) 555-0148</div></div>
          <div class="contact-row"><svg width="14" height="14"><rect x="1" y="3" width="12" height="8" fill="#e7ebf2"/><path d="M1 3l6 5 6-5" stroke="#252e42" fill="none"/></svg><div><b>EMAIL</b>info@bluelanternhour.com</div></div>
          <div class="contact-row"><svg width="14" height="14"><circle cx="7" cy="7" r="6" fill="#e7ebf2"/></svg><div><b>SKYPE</b>bluelanternhour.call</div></div>
          <div class="contact-row"><svg width="14" height="14"><rect x="1" y="2" width="12" height="9" rx="2" fill="#e7ebf2"/></svg><div><b>EVENT COMMENTS</b>Tell us your view</div></div>
          <div class="testimonials">Testimonials &amp; Feedbacks</div>
          Our customers' experience
        </div>
      </article>
      <article class="card">
        <div class="card-head"><svg width="12" height="12"><rect x="1" y="1" width="10" height="10" fill="#f6c300"/></svg>Join Us</div>
        <div class="card-body">
          <b style="color:#e7ebf2">REGISTER NOW</b> and start receiving our monthly motivational article and weekly blog.
          <div class="field-label">NAME</div><div class="field"></div>
          <div class="field-label">EMAIL</div><div class="field"></div>
          <div class="join-lead">Start living each day as your favorite... from TODAY</div>
          <span class="btn">Submit</span>
        </div>
      </article>
    </section>

    <footer class="footer">
      <div class="footer-col" style="left:72px">
        <h3>About Us</h3>
        <ul><li>Home</li><li>The Way</li><li>Live It</li><li>Who Is He</li><li>Contact Me</li><li>Archive</li></ul>
      </div>
      <div class="footer-col" style="left:180px">
        <h3>Categories</h3>
        <ul><li>Live Seminars</li><li>Talk Sessions</li><li>Articles</li><li>Videos</li><li>Coaching Contacts</li><li>Web Based Training</li></ul>
      </div>
      <div class="footer-col" style="left:310px">
        <h3>Affiliated Websites</h3>
        <div class="affiliate-grid">
          <div role="img" aria-label="Affiliate site thumbnail" style="background:linear-gradient(#5b9bd5,#2d5e8e)"></div>
          <div role="img" aria-label="Affiliate site thumbnail" style="background:linear-gradient(#8fc1e8,#3f6f9a)"></div>
          <div role="img" aria-label="Affiliate site thumbnail" style="background:linear-gradient(#6aa8da,#c3d9ec)"></div>
          <div role="img" aria-label="Affiliate site thumbnail" style="background:linear-gradient(#4e86b8,#9fc8e6)"></div>
          <div role="img" aria-label="Affiliate site thumbnail" style="background:linear-gradient(#a8d1ee,#4f7fae)"></div>
          <div role="img" aria-label="Affiliate site thumbnail" style="background:linear-gradient(#3f77a8,#8db9dd)"></div>
          <div role="img" aria-label="Affiliate site thumbnail" style="background:linear-gradient(#78b0de,#2f5a84)"></div>
          <div role="img" aria-label="Affiliate site thumbnail" style="background:linear-gradient(#9cc6e8,#5a8cba)"></div>
        </div>
      </div>
      <div class="footer-col" style="left:570px;width:200px">
        <h3>Latest News &amp; Events</h3>
        <span class="news-badge"></span>
        <ul class="news"><li>• Seminars at The Grand Hall on August 24th</li><li>• Launching of our Web based training</li><li>• Life coach training</li></ul>
      </div>
    </footer>

    <div class="bottom-bar">
      <span>Terms &amp; Conditions &nbsp;|&nbsp; Privacy Policy &nbsp;|&nbsp; Disclaimer</span>
      <span class="bottom-nav"><span>HOME</span><span>THE WAY</span><span>LIVE IT</span><span>WHO IS HE</span><span>CONTACT ME</span><span>ARCHIVE</span></span>
      <span>© 2012 Blue Lantern Hour. All Rights Reserved.</span>
      <span class="bottom-mail"><svg width="12" height="10"><rect x="0.5" y="0.5" width="11" height="9" fill="#fff" stroke="#555"/><path d="M1 1l5 4 5-4" stroke="#555" fill="none"/></svg>info@bluelanternhour.com</span>
    </div>
  </div>
</div>
</body>
</html>
```